Corporate holiday party invitation

Please design a holiday party invitations that looks classy and festive for our member holiday party. The event is first class, semi-formal and needs to be conveyed as such. Please see file from last year so you can see what we are aiming for. The new wording for the invite is as follows: (please use similar fonts to the file provided)

BVK Dallas/Fort Worth
cordially invites you and a guest to the
Yearly Winter Guild Supper Soiree
on Thursday, December 16th
at 6:30pm in the evening

Merrow Tower, Lantern Club
4817 Pell Avenue, 40th floor
Dallas, TX 75288

Tickets are $100 per person and include:
open premium bar, appetizers, three course dinner
and entertainment

Holiday Cocktail Dress

Target Market(s)

middle aged corporate types

Industry/Entity Type

Event

Font styles to use
Script

Requirements
Must have
• Classy holiday feel and design elements,

```html
<!DOCTYPE html>
<html lang="en">
<head>
<meta charset="utf-8">
<title>BVK Dallas/Fort Worth – Yearly Winter Guild Supper Soiree</title>
<link rel="stylesheet" href="https://fonts.googleapis.com/css2?family=Tangerine:wght@400;700&family=Cormorant+Garamond:wght@400;500&display=swap">
<style>
  :root {
    --ink-black: #0d0d0f;
    --charcoal: #2b2b2e;
    --slate: #3d3d41;
    --holiday-red: #b3101a;
    --deep-red: #5a0609;
    --glow-red: #ff3a3a;
    --silver: #c9c9cc;
    --cream: #ece3d2;
  }
  html, body {
    margin: 0;
    padding: 0;
    overflow: hidden;
    background: var(--ink-black);
  }
  .invitation {
    position: relative;
    width: 874px;
    height: 1200px;
    overflow: hidden;
    background:
      radial-gradient(ellipse 520px 420px at 50% 45%, var(--slate) 0%, var(--charcoal) 45%, var(--ink-black) 100%);
    color: var(--cream);
  }
  .bokeh-glow {
    position: absolute;
    border-radius: 50%;
    filter: blur(30px);
  }
  .bokeh-glow--left {
    left: -200px; top: 420px; width: 400px; height: 780px;
    background: radial-gradient(ellipse at 40% 55%, var(--glow-red) 0%, var(--holiday-red) 35%, var(--deep-red) 65%, transparent 80%);
    opacity: 0.8;
  }
  .bokeh-glow--lower-right {
    right: -160px; bottom: -140px; width: 620px; height: 440px;
    background: radial-gradient(ellipse at 60% 60%, var(--glow-red) 0%, var(--holiday-red) 35%, var(--deep-red) 65%, transparent 80%);
    opacity: 0.8;
  }
  .bokeh-glow--top-right {
    right: -120px; top: -80px; width: 420px; height: 300px;
    background: radial-gradient(ellipse, var(--holiday-red) 0%, var(--deep-red) 50%, transparent 78%);
    opacity: 0.75;
  }
  .ornament {
    position: absolute;
    border-radius: 50%;
  }
  .ornament--top-right {
    right: -40px; top: -30px; width: 520px; height: 300px;
    background: radial-gradient(ellipse at 60% 45%, rgba(201,201,204,0.3) 0%, rgba(201,201,204,0.1) 45%, transparent 72%);
  }
  .ornament--bottom-left {
    left: -80px; bottom: -40px; width: 540px; height: 400px;
    background: radial-gradient(ellipse at 40% 60%, rgba(201,201,204,0.28) 0%, rgba(201,201,204,0.1) 45%, transparent 72%);
  }
  .ornament--bottom-right {
    right: -40px; bottom: 70px; width: 440px; height: 280px;
    background: radial-gradient(ellipse at 55% 55%, rgba(201,201,204,0.2) 0%, rgba(201,201,204,0.07) 45%, transparent 72%);
  }
  .sweeps {
    position: absolute;
    inset: 0;
    width: 874px;
    height: 1200px;
  }
  .sweep-band { fill: var(--ink-black); opacity: 0.75; }
  .sweep-line { fill: none; stroke: var(--silver); stroke-linecap: round; }
  .line {
    position: absolute;
    margin: 0;
    white-space: nowrap;
    line-height: 1;
    text-shadow: 0 1px 3px rgba(0,0,0,0.7);
  }
  .script {
    font-family: "Tangerine", cursive;
    font-weight: 700;
  }
  .serif {
    font-family: "Cormorant Garamond", serif;
    font-weight: 500;
  }
  .host        { left: 52px; top: 172px; font-size: 66px; }
  .invite-text { left: 52px; top: 240px; font-size: 54px; }
  .event-name  { left: 52px; top: 296px; font-size: 54px; }
  .event-date  { left: 52px; top: 356px; font-size: 54px; }
  .event-time  { left: 52px; top: 412px; font-size: 54px; }
  .venue       { left: 256px; font-size: 27px; }
  .venue--name    { top: 466px; }
  .venue--street  { top: 516px; }
  .venue--city    { top: 566px; }
  .centered    { left: 280px; width: 600px; text-align: center; font-size: 28px; }
  .tickets     { top: 612px; }
  .inclusions--first  { top: 662px; }
  .inclusions--second { top: 710px; }
  .dress-code  { left: 437px; top: 808px; font-size: 27px; }
</style>
</head>
<body>
<main class="invitation">
  <div class="bokeh-glow bokeh-glow--left" role="img" aria-label="Soft red holiday bokeh lights"></div>
  <div class="bokeh-glow bokeh-glow--lower-right" role="img" aria-label="Soft red holiday bokeh lights"></div>
  <div class="bokeh-glow bokeh-glow--top-right" role="img" aria-label="Soft red holiday bokeh lights"></div>
  <div class="ornament ornament--top-right" role="img" aria-label="Silver flourish swirl ornament"></div>
  <div class="ornament ornament--bottom-left" role="img" aria-label="Silver flourish swirl ornament"></div>
  <div class="ornament ornament--bottom-right" role="img" aria-label="Silver flourish swirl ornament"></div>

  <svg class="sweeps" viewBox="0 0 874 1200" aria-hidden="true">
    <path class="sweep-band" d="M0 20 C220 170 560 150 874 -10 L874 40 C600 190 250 220 0 80 Z"/>
    <path class="sweep-line" stroke-width="3" opacity="0.55" d="M0 70 C240 210 580 180 874 20"/>
    <path class="sweep-line" stroke-width="1.5" opacity="0.35" d="M40 110 C280 230 600 200 874 70"/>
    <path class="sweep-band" d="M0 1010 C260 900 560 900 874 840 L874 900 C580 960 280 960 0 1080 Z"/>
    <path class="sweep-line" stroke-width="3" opacity="0.5" d="M0 1000 C260 890 560 890 874 830"/>
    <path class="sweep-line" stroke-width="1.5" opacity="0.35" d="M0 1090 C300 970 600 960 874 910"/>
  </svg>

  <h1 class="line script host">BVK Dallas/Fort Worth</h1>
  <p class="line script invite-text">cordially invites you and a guest to the</p>
  <p class="line script event-name">Yearly Winter Guild Supper Soiree</p>
  <p class="line script event-date">on Thursday, December 16th</p>
  <p class="line script event-time">at 6:30pm in the evening</p>

  <p class="line serif venue venue--name">Merrow Tower, Lantern Club</p>
  <p class="line serif venue venue--street">4817 Pell Avenue, 40th floor</p>
  <p class="line serif venue venue--city">Dallas, TX 75288</p>

  <p class="line serif centered tickets">Tickets are $100 per person and include:</p>
  <p class="line serif centered inclusions--first">open premium bar, appetizers, three course dinner</p>
  <p class="line serif centered inclusions--second">and entertainment</p>

  <p class="line serif dress-code">Holiday Cocktail Dress</p>
</main>
</body>
</html>
```